Uprising SaaS company needs an attractive business card design

We're an uprising SaaS company who's attempting to attack the rigid car (insurance) claims management market in Europe.
We want to our mighty base order management system, listen to our clients to connect the smart ideas to build something even mightier.
We primarily focus on helping our customers manage their customers' claims/orders and get them resolved as smoothly as possible.
We'd like the business card design to express technical innovation and the fact that we connect smart ideas, as our company slogan indicates.
Contact Information for Business Card
Name, position, website, email, mobile, business address
Font styles to use
Colors
Designer to choose colors to be used in the design.
Look and feel
Each slider illustrates characteristics of the customer's brand and the style your logo design should communicate.

```html
<!DOCTYPE html>
<html lang="en">
<head>
<meta charset="utf-8">
<title>Quilsora Business Card</title>
<link href="https://fonts.googleapis.com/css2?family=Montserrat:wght@400;700&display=swap" rel="stylesheet">
<style>
  :root {
    --card-black: #0a0a0a;
    --brand-blue: #82d0e4;
    --text-white: #ffffff;
    --stage: #ececec;
  }
  * { margin: 0; padding: 0; box-sizing: border-box; }
  html, body {
    width: 1200px; height: 728px; overflow: hidden;
    background: var(--stage);
    font-family: "Montserrat", sans-serif;
  }
  .card {
    position: absolute;
    top: 210px;
    width: 511px; height: 307px;
    background: var(--card-black);
    overflow: hidden;
  }
  .card--front { left: 72px; }
  .card--back { left: 617px; }

  .brand-band {
    position: absolute; left: 0; top: 113px;
    width: 269px; height: 85px;
    background: var(--brand-blue);
    border-radius: 0 6px 6px 0;
  }
  .wordmark {
    position: absolute;
    font-weight: 400;
    font-size: 48px;
    letter-spacing: 0.5px;
    line-height: 1;
    white-space: nowrap;
  }
  .brand-band .wordmark { left: 34px; top: 24px; color: var(--card-black); }

  .holder { position: absolute; left: 287px; top: 88px; color: var(--text-white); }
  .holder__name {
    font-weight: 700; font-size: 27px; letter-spacing: 0.5px; line-height: 1.1;
    text-transform: uppercase; white-space: nowrap;
  }
  .holder__name .surname { color: var(--brand-blue); }
  .holder__role { font-size: 15px; margin-top: 4px; letter-spacing: 0.3px; line-height: 1.2; }

  .contact-list { list-style: none; margin-top: 12px; }
  .contact-list li {
    display: flex; align-items: center; gap: 5px;
    font-size: 15px; letter-spacing: 0.3px; height: 22px; white-space: nowrap;
  }
  .contact-icon { width: 13px; height: 13px; flex: none; }

  .card--back .wordmark { left: 64px; top: 136px; color: var(--text-white); }
  .slogan-band {
    position: absolute; left: 268px; top: 153px;
    width: 243px; height: 20px;
    background: var(--brand-blue);
    border-radius: 4px 0 0 4px;
    color: var(--card-black);
    font-size: 12px; letter-spacing: 0.4px;
    line-height: 20px; padding-left: 12px;
    text-transform: uppercase; white-space: nowrap;
  }
</style>
</head>
<body>
  <section class="card card--front">
    <div class="brand-band">
      <span class="wordmark">quilsora</span>
    </div>
    <div class="holder">
      <h1 class="holder__name">Lena <span class="surname">Voss</span></h1>
      <p class="holder__role">CEO/Onwer</p>
      <ul class="contact-list">
        <li>
          <svg class="contact-icon" viewBox="0 0 16 16" aria-hidden="true">
            <circle cx="8" cy="8" r="8" fill="var(--brand-blue)"/>
            <path d="M5.2 3.8l1.5 1.7-.8 1.1c.5 1.2 1.4 2.1 2.6 2.6l1.1-.8 1.7 1.5-.7 1.5c-3.4-.2-6.3-3.1-6.5-6.5z" fill="var(--card-black)"/>
          </svg>
          (555) 014-2290
        </li>
        <li>
          <svg class="contact-icon" viewBox="0 0 16 16" aria-hidden="true">
            <circle cx="8" cy="8" r="8" fill="var(--brand-blue)"/>
            <rect x="4" y="5.2" width="8" height="5.6" fill="none" stroke="var(--card-black)" stroke-width="1.1"/>
            <path d="M4 5.4L8 8.6 12 5.4" fill="none" stroke="var(--card-black)" stroke-width="1.1"/>
          </svg>
          hello@quilsora.com
        </li>
        <li>
          <svg class="contact-icon" viewBox="0 0 16 16" aria-hidden="true">
            <circle cx="8" cy="8" r="8" fill="var(--brand-blue)"/>
            <g fill="none" stroke="var(--card-black)" stroke-width="0.9">
              <circle cx="8" cy="8" r="4.3"/>
              <ellipse cx="8" cy="8" rx="1.9" ry="4.3"/>
              <path d="M3.7 8h8.6M4.3 5.8h7.4M4.3 10.2h7.4"/>
            </g>
          </svg>
          www.quilsora.com
        </li>
      </ul>
    </div>
  </section>

  <section class="card card--back">
    <span class="wordmark">quilsora</span>
    <p class="slogan-band">Our company slogan</p>
  </section>
</body>
</html>
```